TidePost RV/Boat/Auto Storage

Front page for web site. Looking for a modern, clean design. Want rotating photo section (see attached) and all components similar to this web site, BUT NOT THE SAME:
https://www.marlowdepot.example/

This is a fully enclosed, for lease project. They are not condominiums for sale, or "self-storage" units. Logo and sample images are attached for your use.

Target Market(s)

Affluent customers who have high-end RV's (main focus), boats ,or automobiles.

Industry/Entity Type

Commercial real estate.

Coding

Coded - Design and coding required

Number of Pages Required

1 page

```html
<!DOCTYPE html>
<html lang="en">
<head>
<meta charset="utf-8">
<title>TidePost RV/Boat/Auto Storage</title>
<link rel="stylesheet" href="https://fonts.googleapis.com/css2?family=Alegreya:wght@400;500&family=Poppins:wght@300;400;500&display=swap">
<style>
:root{
  --nav:#344a43;
  --ink:#1f3733;
  --btn:#1e3934;
  --about-bg:#effafc;
  --gallery-bg:#eaeaea;
  --cta:#2e4a45;
  --footer:#0f3a3b;
  --text:#2a2a2a;
  --white:#ffffff;
  --serif:'Alegreya', Georgia, serif;
  --sans:'Poppins', Arial, sans-serif;
}
*{margin:0;padding:0;box-sizing:border-box}
html,body{width:1200px;height:4955px;overflow:hidden}
body{position:relative;font-family:var(--sans);color:var(--text);background:var(--white)}
h1,h2,h3,h4{font-weight:400}
.pill{position:absolute;display:flex;align-items:center;justify-content:center;background:var(--btn);color:var(--white);border-radius:40px;font-family:var(--sans)}

/* nav */
.site-nav{position:absolute;left:0;top:0;width:1200px;height:110px;background:var(--nav)}
.brand{position:absolute;font-family:var(--serif);color:var(--white);font-size:30px;letter-spacing:1px}
.site-nav .brand{left:69px;top:34px}
.nav-links{position:absolute;left:514px;top:45px;font-size:13px;color:var(--white)}
.nav-links span{position:absolute;white-space:nowrap}
.nav-links .active{border-bottom:1px solid var(--white);padding-bottom:2px}
.nav-contact{position:absolute;left:1024px;top:37px;width:110px;height:34px;border:1.5px solid var(--white);border-radius:20px;color:var(--white);font-size:13px;display:flex;align-items:center;justify-content:center;background:#233a35}

/* hero */
.hero{position:absolute;left:0;top:110px;width:1200px;height:675px;overflow:hidden;background:linear-gradient(180deg,#5d7584 0%,#8aa3ae 45%,#5f8596 60%,#3f6e80 100%)}
.hero-glow{position:absolute;left:215px;top:-60px;width:770px;height:770px;border-radius:50%;background:radial-gradient(circle,rgba(240,248,250,.75) 0%,rgba(225,240,245,.6) 70%,rgba(225,240,245,.3) 100%)}
.hero h1{position:absolute;left:0;top:185px;width:1200px;text-align:center;font-family:var(--serif);font-size:100px;line-height:115px;color:var(--ink)}
.hero .pill{left:467px;top:468px;width:266px;height:67px;font-size:32px}

/* about */
.about{position:absolute;left:0;top:785px;width:1200px;height:531px;background:var(--about-bg)}
.about h2{position:absolute;left:97px;top:65px;font-family:var(--serif);font-size:66px;color:var(--ink)}
.about p{position:absolute;left:90px;top:168px;width:510px;font-size:13.4px;line-height:22.7px;text-align:justify;color:#333}
.about .pill{left:93px;top:425px;width:135px;height:40px;font-size:13px}
.about-ring{position:absolute;left:653px;top:23px;width:445px;height:445px;border-radius:50%;border:2px solid var(--ink)}
.about-photo{position:absolute;left:669px;top:39px;width:413px;height:413px;border-radius:50%;background:radial-gradient(circle at 60% 55%,#7a1b1b 0%,#2b2b2b 35%,#1a1a1a 70%,#4a4a4a 100%)}

/* banners */
.banner{position:absolute;left:0;width:1200px;overflow:hidden}
.banner h2{position:absolute;left:0;width:1200px;text-align:center;font-family:var(--serif);font-size:92px;color:var(--ink)}
.banner-amen{top:1316px;height:274px;background:linear-gradient(180deg,#9fc7d0 0%,#c7e3e8 45%,#b9d3d8 100%)}
.banner-amen h2{top:80px}
.banner-loc{top:3475px;height:288px;background:linear-gradient(90deg,#c8d9e2 0%,#dfe9ef 50%,#b9cedb 100%)}
.banner-loc h2{top:85px}

/* amenities */
.amen-title{position:absolute;left:0;top:1618px;width:1200px;text-align:center;font-size:54px;color:var(--ink)}
.amen-sub{position:absolute;left:180px;top:1705px;width:840px;text-align:center;font-size:16.5px;line-height:20px;color:#222}
.amen-list{position:absolute;list-style:none;width:400px}
.amen-list li{position:relative;height:53px;padding-left:37px;font-size:15.5px;line-height:19px;color:#333}
.amen-list li::before{content:"";position:absolute;left:0;top:5px;width:12px;height:12px;border-radius:50%;background:var(--ink)}
.amen-left{left:145px;top:1802px}
.amen-right{left:658px;top:1802px}

/* gallery */
.gallery{position:absolute;left:0;top:2100px;width:1200px;height:723px;background:var(--gallery-bg)}
.gallery h2{position:absolute;left:0;top:55px;width:1200px;text-align:center;font-family:var(--serif);font-size:66px;color:var(--ink)}
.tile{position:absolute;width:297px;height:190px}
.t-rv{background:linear-gradient(180deg,#6c7a55 0%,#8a8a70 50%,#4d5a3a 100%)}
.t-boat{background:linear-gradient(180deg,#5d7380 0%,#9fb4bd 55%,#3f6b7b 100%)}
.t-car{background:radial-gradient(circle at 60% 60%,#8a1c1c 0%,#2a2a2a 40%,#1c1c1c 100%)}
.gallery .pill{left:515px;top:620px;width:207px;height:45px;font-size:19px}

/* categories */
.card{position:absolute;top:2900px;width:311px;height:480px;background:var(--white);border-radius:6px;box-shadow:0 0 12px rgba(0,0,0,.14)}
.card .tile{left:19px;top:27px;width:270px;height:180px}
.card h3{position:absolute;left:0;top:222px;width:100%;text-align:center;font-size:40px;color:var(--ink)}
.card p{position:absolute;left:22px;top:284px;width:267px;text-align:center;font-size:13.4px;line-height:22.7px;color:#333}
.card .pill{left:97px;top:413px;width:118px;height:32px;font-size:12.5px}

/* location */
.loc-title{position:absolute;left:0;top:3815px;width:1200px;text-align:center;font-size:40px;color:var(--ink)}
.loc-text{position:absolute;left:180px;top:3890px;width:840px;text-align:center;font-size:13.4px;line-height:20px;color:#333}
.map{position:absolute;left:157px;top:3975px;width:914px;height:335px;background:linear-gradient(135deg,#cfe6c8 0%,#e8ead8 40%,#d6ecd0 70%,#c4e1c2 100%)}

/* cta */
.cta{position:absolute;left:0;top:4368px;width:1200px;height:102px;background:var(--cta)}
.cta p{position:absolute;left:67px;top:34px;font-size:27px;color:var(--white);font-weight:300}
.cta .pill{left:870px;top:33px;width:263px;height:43px;font-size:19px;background:#142d2a}

/* footer */
.footer{position:absolute;left:0;top:4470px;width:1200px;height:485px;background:var(--footer);color:var(--white)}
.footer .brand{left:138px;top:155px;font-size:31px}
.social{position:absolute;top:224px;width:36px;height:36px;border-radius:50%;background:var(--white)}
.footer h4{position:absolute;top:104px;font-size:20px;font-weight:500}
.foot-links{position:absolute;left:511px;top:152px;list-style:none}
.foot-links li{position:relative;padding-left:18px;height:32.5px;font-size:17px}
.foot-links li::before{content:"";position:absolute;left:0;top:10px;width:7px;height:7px;border-radius:50%;background:var(--white)}
.contact-item{position:absolute;left:822px;font-size:16.5px;line-height:24px}
.contact-item svg{position:absolute;left:0;top:0}
.contact-item div{margin-left:48px}
.footer hr{position:absolute;left:67px;top:405px;width:1066px;border:0;border-top:1px solid rgba(255,255,255,.25)}
.copy{position:absolute;left:0;top:433px;width:1200px;text-align:center;font-size:13px}
</style>
</head>
<body>

<header class="site-nav">
  <div class="brand">TIDEPOST</div>
  <nav class="nav-links">
    <span class="active" style="left:0">Home</span>
    <span style="left:71px">About Us</span>
    <span style="left:168px">Amenities</span>
    <span style="left:263px">Gallery</span>
    <span style="left:359px">News</span>
    <span style="left:432px">Owner</span>
  </nav>
  <div class="nav-contact">Contact Us</div>
</header>

<section class="hero" role="img" aria-label="Photo of a white center-console boat on open water under a cloudy sky">
  <div class="hero-glow"></div>
  <h1>Find Amazing<br>Parking Space</h1>
  <div class="pill">Know More</div>
</section>

<section class="about">
  <h2>About Us</h2>
  <p>On the other hand, we denounce with righteous indignation and dislike men who are so beguiled and demoralized by the charms of pleasure of the moment, so blinded by desire, that they cannot foresee the pain and trouble that are bound to ensue; and equal blame belongs to those who fail in their duty through weakness of will, which is the same as saying through shrinking from toil and pain. These cases are perfectly simple and easy to distinguish.On the other hand, we denounce with righteous indignation and dislike men who are so beguiled and demoralized by the charms of pleasure of the moment, so blinded by desire, that they cannot foresee the pain and trouble that are bound to ensue; and equal blame</p>
  <div class="pill">Read More</div>
  <div class="about-ring"></div>
  <div class="about-photo" role="img" aria-label="Photo of a sports car under a black and red fitted cover"></div>
</section>

<section class="banner banner-amen" role="img" aria-label="Photo of a bright covered parking garage with columns">
  <h2>Amenities</h2>
</section>

<h2 class="amen-title">More than just a storage complex.</h2>
<p class="amen-sub">when our power of choice is untrammelled and when nothing prevents our being able to do what we like best, every pleasure is to be welcomed and every pain avoided.</p>
<ul class="amen-list amen-left">
  <li>Lorem Ipsum has been the industry's standard dummy text ever since the 1500s, when an</li>
  <li>Lorem Ipsum has been the industry's standard dummy text ever since the 1500s, when an</li>
  <li>Lorem Ipsum has been the industry's standard dummy text ever since the 1500s, when an</li>
  <li>Lorem Ipsum has been the industry's standard dummy text ever since the 1500s, when an</li>
  <li>Lorem Ipsum has been the industry's standard dummy text ever since the 1500s, when an</li>
</ul>
<ul class="amen-list amen-right">
  <li>Lorem Ipsum has been the industry's standard dummy text ever since the 1500s, when an</li>
  <li>Lorem Ipsum has been the industry's standard dummy text ever since the 1500s, when an</li>
  <li>Lorem Ipsum has been the industry's standard dummy text ever since the 1500s, when an</li>
  <li>Lorem Ipsum has been the industry's standard dummy text ever since the 1500s, when an</li>
  <li>Lorem Ipsum has been the industry's standard dummy text ever since the 1500s, when an</li>
</ul>

<section class="gallery">
  <h2>Gallery</h2>
  <div class="tile t-rv" style="left:137px;top:166px" role="img" aria-label="Photo of a luxury motorhome parked under trees"></div>
  <div class="tile t-boat" style="left:456px;top:166px" role="img" aria-label="Photo of a white boat on the water"></div>
  <div class="tile t-car" style="left:775px;top:166px" role="img" aria-label="Photo of a covered sports car"></div>
  <div class="tile t-boat" style="left:137px;top:380px" role="img" aria-label="Photo of a white boat on the water"></div>
  <div class="tile t-car" style="left:456px;top:380px" role="img" aria-label="Photo of a covered sports car"></div>
  <div class="tile t-rv" style="left:775px;top:380px" role="img" aria-label="Photo of a luxury motorhome parked under trees"></div>
  <div class="pill">View More</div>
</section>

<article class="card" style="left:111px">
  <div class="tile t-car" role="img" aria-label="Photo of a covered sports car"></div>
  <h3>Cars</h3>
  <p>Lorem ipsum dolor sit amet, consectetur adipiscing elit, sed do eiusmod tempor incididunt ut labore et dolore magna aliqua. Quis ipsum suspendisse ultrices gravida. Risus</p>
  <div class="pill">Read More</div>
</article>
<article class="card" style="left:448px">
  <div class="tile t-boat" role="img" aria-label="Photo of a white boat on the water"></div>
  <h3>Boats</h3>
  <p>Lorem ipsum dolor sit amet, consectetur adipiscing elit, sed do eiusmod tempor incididunt ut labore et dolore magna aliqua. Quis ipsum suspendisse ultrices gravida. Risus</p>
  <div class="pill">Read More</div>
</article>
<article class="card" style="left:786px">
  <div class="tile t-rv" role="img" aria-label="Photo of a luxury motorhome parked under trees"></div>
  <h3>RVs</h3>
  <p>Lorem ipsum dolor sit amet, consectetur adipiscing elit, sed do eiusmod tempor incididunt ut labore et dolore magna aliqua. Quis ipsum suspendisse ultrices gravida. Risus</p>
  <div class="pill">Read More</div>
</article>

<section class="banner banner-loc" role="img" aria-label="Photo of a clean indoor storage hall with overhead lights">
  <h2>Location</h2>
</section>

<h2 class="loc-title">Living it up in Fort Myers, Florida.</h2>
<p class="loc-text">Lorem ipsum dolor sit amet, consectetur adipiscing elit, sed do eiusmod tempor incididunt ut labore et dolore magna aliqua. Quis ipsum suspendisse ultrices gravida. Risus commodo viverra maecenas accumsan lacus vel facilisis.</p>
<div class="map" role="img" aria-label="Map showing the storage facility location"></div>

<section class="cta">
  <p>Your vehicle's new home awaits.</p>
  <div class="pill">Start The Process</div>
</section>

<footer class="footer">
  <div class="brand">TIDEPOST</div>
  <div class="social" style="left:167px"></div>
  <div class="social" style="left:216px"></div>
  <div class="social" style="left:263px"></div>

  <h4 style="left:514px">LINKS</h4>
  <ul class="foot-links">
    <li>About Us</li>
    <li>Amenities</li>
    <li>Gallery</li>
    <li>News</li>
    <li>Onwer</li>
    <li>Contact Us</li>
  </ul>

  <h4 style="left:811px">CONTACT US</h4>
  <div class="contact-item" style="top:162px">
    <svg width="36" height="36" viewBox="0 0 36 36"><circle cx="18" cy="18" r="18" fill="#fff"/><path d="M18 8a7 7 0 0 0-7 7c0 5 7 13 7 13s7-8 7-13a7 7 0 0 0-7-7zm0 9.5a2.5 2.5 0 1 1 0-5 2.5 2.5 0 0 1 0 5z" fill="#0f3a3b"/></svg>
    <div>ADDRESS:<br>27/8 Harbor Lane,<br>FL 33901</div>
  </div>
  <div class="contact-item" style="top:256px">
    <svg width="36" height="36" viewBox="0 0 36 36"><circle cx="18" cy="18" r="18" fill="#fff"/><path d="M12.5 9.5l3 0 1.5 4.5-2 1.5c1 2.2 2.8 4 5 5l1.5-2 4.5 1.5v3c0 1-1 2-2 2C16 25 11 20 10.5 12c0-1.5 1-2.5 2-2.5z" fill="#0f3a3b"/></svg>
    <div>PHONE:<br>+1 555 014 2290</div>
  </div>
  <div class="contact-item" style="top:326px">
    <svg width="36" height="36" viewBox="0 0 36 36"><circle cx="18" cy="18" r="18" fill="#fff"/><rect x="9" y="12" width="18" height="12" rx="1.5" fill="#0f3a3b"/><path d="M9.5 12.5l8.5 6.5 8.5-6.5" fill="none" stroke="#fff" stroke-width="1.4"/></svg>
    <div>EMAIL:<br>info@tidepost.example</div>
  </div>

  <hr>
  <p class="copy">© 2024 Company Name, Inc. All Rights Reserved.</p>
</footer>

</body>
</html>
```